Ren's Moroccan Night 30th Birthday Bash

We need an invitation that compliments a start studded guest list of the most influential 20-30 year olds in manhattan. The theme of the party is moroccan nights with black and gold color scheme. 9pm - all night, cocktails and horderves followed by Dj Olvan and surprise entertainment. Attire gypsy chic. Address will be provided upon RSVP

Font styles to use
Decorative
Script

Colors
fbed22
000000

Requirements
Should not have
• basic

```html
<!DOCTYPE html>
<html lang="en">
<head>
<meta charset="utf-8">
<title>Moroccan Night – Ren's 30th Birthday</title>
<link rel="stylesheet" href="https://fonts.googleapis.com/css2?family=Russo+One&family=Lato:wght@300;400;700&family=Berkshire+Swash&display=swap">
<style>
  :root {
    --navy-deep: #02142a;
    --navy-mid: #033252;
    --teal-blue: #065a7e;
    --gold: #d3b14f;
    --gold-soft: #c8a648;
    --pattern-dark: #0a2f54;
    --pattern-light: #1a5a86;
  }
  * { margin: 0; padding: 0; box-sizing: border-box; }
  html, body { width: 857px; height: 1200px; overflow: hidden; }
  body {
    background: var(--navy-deep);
    font-family: "Lato", sans-serif;
  }
  .invitation {
    position: relative;
    width: 857px;
    height: 1200px;
    overflow: hidden;
    background: linear-gradient(170deg, var(--navy-deep) 0%, var(--navy-mid) 45%, var(--teal-blue) 78%, #05567a 100%);
    color: var(--gold);
    text-align: center;
  }
  .crest-ornament {
    position: absolute;
    left: 345px;
    top: 118px;
    width: 168px;
    height: 92px;
    border-radius: 40% 40% 30% 30%;
    background: radial-gradient(ellipse at center, rgba(211,177,79,0.55) 0%, rgba(211,177,79,0.25) 60%, rgba(211,177,79,0) 100%);
  }
  .event-title {
    position: absolute;
    top: 218px;
    left: 0;
    width: 100%;
    font-family: "Russo One", sans-serif;
    font-size: 56px;
    letter-spacing: 3px;
    line-height: 1;
    color: var(--gold);
  }
  .medallion {
    position: absolute;
    left: 0;
    top: 0;
    width: 857px;
    height: 1200px;
  }
  .medallion-text {
    position: absolute;
    top: 452px;
    left: 0;
    width: 100%;
  }
  .celebrant {
    font-weight: 700;
    font-size: 52px;
    line-height: 67px;
    letter-spacing: 1px;
  }
  .timing {
    margin-top: 20px;
    font-size: 27px;
    line-height: 42px;
    font-weight: 400;
  }
  .program {
    position: absolute;
    top: 918px;
    left: 0;
    width: 100%;
    font-weight: 300;
    font-size: 29px;
    line-height: 41px;
    color: var(--gold-soft);
  }
  .amp {
    font-family: "Berkshire Swash", cursive;
    font-size: 30px;
  }
  .attire {
    position: absolute;
    top: 1040px;
    left: 0;
    width: 100%;
    font-family: "Berkshire Swash", cursive;
    font-size: 30px;
    color: var(--gold);
  }
</style>
</head>
<body>
  <main class="invitation">
    <div class="crest-ornament" role="img" aria-label="Gold lattice filigree ornament"></div>

    <h1 class="event-title">MOROCCAN NIGHT</h1>

    <svg class="medallion" viewBox="0 0 857 1200" aria-hidden="true">
      <defs>
        <radialGradient id="medallion-fill" cx="50%" cy="50%" r="60%">
          <stop offset="0%" stop-color="var(--pattern-dark)"/>
          <stop offset="100%" stop-color="var(--pattern-light)"/>
        </radialGradient>
        <path id="medallion-shape" d="M 310 345 Q 428 320 546 345 C 570 350 575 375 600 380 C 660 385 700 400 700 440 C 700 470 690 470 700 490 C 730 560 730 640 700 710 C 690 730 700 730 700 760 C 700 800 660 815 600 820 C 575 825 570 850 546 855 Q 428 880 310 855 C 286 850 281 825 256 820 C 196 815 156 800 156 760 C 156 730 166 730 156 710 C 126 640 126 560 156 490 C 166 470 156 470 156 440 C 156 400 196 385 256 380 C 281 375 286 350 310 345 Z"/>
      </defs>
      <g role="img" aria-label="Moroccan star lattice pattern inside the medallion">
        <use href="#medallion-shape" fill="url(#medallion-fill)"/>
      </g>
      <use href="#medallion-shape" fill="none" stroke="#d3b14f" stroke-width="3"/>
      <use href="#medallion-shape" fill="none" stroke="#d3b14f" stroke-width="12"
           transform="translate(428 600) scale(0.9 0.9) translate(-428 -600)"/>
    </svg>

    <div class="medallion-text">
      <p class="celebrant">Ren’s<br>30th<br>Birthday</p>
      <p class="timing">Party All Night<br>Starting at 9 PM</p>
    </div>

    <div class="program">
      <p>Cocktails <span class="amp">&amp;</span> Hors d'oeuvre</p>
      <p>Dj Olvan <span class="amp">&amp;</span> Surprise Entertainment</p>
    </div>

    <p class="attire">Attire:&nbsp; Gypsy Chic</p>
  </main>
</body>
</html>
```